Norvane Builders Business Card

Modern and Professional Business Card for a Med size construction/development company.

See the samples below for the design I like … but I need ideas for incorporating the red company logo while still keeping the clean look of the card samples that are attached.

Logo and tag line on the back … info on the front.

Tagline: Quality Starts from the Ground Up

Target Market(s)

Med-Large General Contractors

Contact Information for Business Card

Norvane Builders Limited
42 Brenton Street
Elk Harbour, NL
B3K 7T2

t: 709-555-0147
f: 709-555-0192
w: www.norvanebuilders-example.com

Font styles to use
Sans Serif

Colors
fbee3e

Requirements
Must have
• I like the black and yellow designs of the attached samples …. but I'm not sure how to incorporate the red Norvane Builders logo into that design??
Nice to have
• Construction safety strips

```html
<!DOCTYPE html>
<html lang="en">
<head>
<meta charset="utf-8">
<title>Norvane Builders Business Card</title>
<link href="https://fonts.googleapis.com/css2?family=Montserrat:wght@400;500;700;800&family=Oswald:wght@500&display=swap" rel="stylesheet">
<style>
  :root {
    --stage: #2a2c30;
    --card: #070707;
    --yellow: #fbee3e;
    --red: #e0222b;
    --white: #f2f2f2;
    --grey: #d6d6d6;
  }
  * { box-sizing: border-box; margin: 0; padding: 0; }
  html, body { width: 1200px; height: 900px; overflow: hidden; }
  body {
    background: var(--stage);
    font-family: "Montserrat", sans-serif;
    position: relative;
  }
  .card {
    position: absolute;
    left: 280px;
    width: 640px;
    height: 366px;
    background: var(--card);
    border-radius: 4px;
    box-shadow: 0 18px 40px rgba(0,0,0,.45);
    overflow: hidden;
  }
  .card--back { top: 60px; }
  .card--front { top: 470px; }

  /* Brand name block */
  .brand {
    position: absolute;
    display: flex;
    align-items: center;
    gap: 14px;
  }
  .brand__mark {
    width: 22px;
    height: 22px;
    background: var(--red);
    flex: none;
  }
  .brand__name {
    font-weight: 800;
    color: var(--white);
    text-transform: uppercase;
    letter-spacing: 1px;
    line-height: 1.05;
  }
  .card--back .brand { left: 0; right: 0; top: 110px; justify-content: center; }
  .card--back .brand__name { font-size: 34px; }
  .card--front .brand { left: 40px; top: 40px; }
  .card--front .brand__name { font-size: 24px; }

  /* Back: safety strip with tagline */
  .safety-row {
    position: absolute;
    left: 0; right: 0; top: 262px;
    height: 22px;
    display: flex;
    align-items: center;
  }
  .safety-strip {
    height: 16px;
    background: repeating-linear-gradient(-60deg, var(--yellow) 0 5px, transparent 5px 11px);
  }
  .safety-strip--lead { width: 150px; }
  .safety-strip--tail { flex: 1; }
  .tagline {
    font-family: "Oswald", sans-serif;
    font-weight: 500;
    font-size: 20px;
    color: var(--yellow);
    text-transform: uppercase;
    letter-spacing: .3px;
    padding: 0 20px;
    white-space: nowrap;
  }

  /* Front: dashed divider */
  .divider { position: absolute; left: 0; top: 0; }

  .contact {
    position: absolute;
    left: 40px; top: 232px;
    list-style: none;
    font-size: 15px;
    color: var(--white);
  }
  .contact li { display: flex; align-items: center; gap: 10px; margin-bottom: 9px; }
  .contact svg { width: 14px; height: 14px; flex: none; }

  .person {
    position: absolute;
    right: 40px; top: 218px;
    text-align: right;
  }
  .person__name {
    font-weight: 700;
    font-size: 19px;
    color: var(--yellow);
    text-transform: uppercase;
    letter-spacing: 1px;
  }
  .person__role {
    font-size: 16px;
    color: var(--red);
    margin-bottom: 6px;
  }
  .person__address {
    font-style: normal;
    font-size: 16px;
    color: var(--grey);
    line-height: 1.35;
  }
</style>
</head>
<body>

  <section class="card card--back" aria-label="Card back">
    <div class="brand">
      <span class="brand__mark"></span>
      <span class="brand__name">Norvane Builders Limited</span>
    </div>
    <div class="safety-row">
      <span class="safety-strip safety-strip--lead"></span>
      <span class="tagline">Quality Starts from the Ground Up</span>
      <span class="safety-strip safety-strip--tail"></span>
    </div>
  </section>

  <section class="card card--front" aria-label="Card front">
    <div class="brand">
      <span class="brand__mark"></span>
      <span class="brand__name">Norvane<br>Builders Limited</span>
    </div>

    <svg class="divider" width="640" height="366" viewBox="0 0 640 366" aria-hidden="true">
      <line x1="40" y1="150" x2="450" y2="210" stroke="#fbee3e" stroke-width="7" stroke-dasharray="18 12"/>
    </svg>

    <ul class="contact">
      <li>
        <svg viewBox="0 0 14 14" aria-hidden="true"><circle cx="7" cy="7" r="7" fill="#e0222b"/><path d="M4.5 3.5l1.5 0 .6 2-1 .8a5 5 0 0 0 2.1 2.1l.8-1 2 .6 0 1.5c-3.5.3-6.3-2.5-6-6z" fill="#070707"/></svg>
        709-555-0147
      </li>
      <li>
        <svg viewBox="0 0 14 14" aria-hidden="true"><rect x="4" y="1.5" width="6" height="4" fill="#e0222b"/><rect x="1.5" y="5" width="11" height="5" rx="1" fill="#e0222b"/><rect x="4" y="9" width="6" height="3.5" fill="#e0222b"/></svg>
        709-555-0192
      </li>
      <li>
        <svg viewBox="0 0 14 14" aria-hidden="true"><circle cx="7" cy="7" r="6.5" fill="#e0222b"/><path d="M.5 7h13M7 .5v13M7 .5c-3 3.5-3 9.5 0 13M7 .5c3 3.5 3 9.5 0 13" stroke="#070707" stroke-width="1" fill="none"/></svg>
        www.norvanebuilders-example.com
      </li>
    </ul>

    <div class="person">
      <p class="person__name">Dana Whitlock</p>
      <p class="person__role">President</p>
      <address class="person__address">
        42 Brenton Street<br>
        Elk Harbour, NL<br>
        B3K 7T2
      </address>
    </div>
  </section>

</body>
</html>
```